Brisco Interiors

Hi, can you please make this design up for me. Brisco interiors text to front and Philippa Brisco text to back in black. Small love hearts to be black. Mobile number to front text and back mobile number and email address text to be white. Open to your input 🙂 Thanks in advance! Philippa

Industry/Entity Type

Interior Design

Colors

Designer to choose only greyscale colors for use in the design.

Requirements
Must have
• Little love hearts for dot on i

```html
<!DOCTYPE html>
<html lang="en">
<head>
<meta charset="utf-8">
<title>Brisco Interiors – Business Card</title>
<link href="https://fonts.googleapis.com/css2?family=Montserrat:wght@300;400&display=swap" rel="stylesheet">
<style>
  :root {
    --stage: #1c1c1c;
    --card-dark: #141414;
    --card-light: #ffffff;
    --ink: #1a1a1a;
    --ink-soft: #8a8a8a;
    --logo-light: #d9d9d9;
    --logo-dark: #6e6e6e;
    --rule: #9a9a9a;
    --band: #111111;
  }
  * { margin: 0; padding: 0; box-sizing: border-box; }
  html, body {
    width: 1200px; height: 900px; overflow: hidden;
    background: var(--stage);
    font-family: "Montserrat", sans-serif;
  }
  .stage {
    position: relative; width: 1200px; height: 900px;
    display: flex; flex-direction: column; align-items: center; justify-content: center; gap: 40px;
  }
  .card {
    position: relative; width: 680px; height: 389px; overflow: hidden;
    box-shadow: 0 18px 40px rgba(0,0,0,.55);
  }
  .card--front { background: var(--card-dark); }
  .card--back { background: var(--card-light); }

  .wordmark {
    position: absolute; display: flex; align-items: center; gap: 12px;
    font-weight: 300; letter-spacing: 2px; text-transform: uppercase; white-space: nowrap;
  }
  .wordmark__dot { width: 10px; height: 10px; border-radius: 50%; }
  .card--front .wordmark { left: 190px; top: 150px; font-size: 30px; color: var(--logo-light); }
  .card--front .wordmark__dot { background: var(--logo-light); }
  .card--back .wordmark { left: 330px; top: 52px; font-size: 22px; color: var(--logo-dark); }
  .card--back .wordmark__dot { background: var(--logo-dark); width: 8px; height: 8px; }

  .person { position: absolute; left: 322px; top: 150px; }
  .person__name {
    font-size: 21px; font-weight: 400; letter-spacing: 2.5px; text-transform: uppercase; color: var(--ink);
  }
  .person__role { font-size: 14px; font-weight: 300; color: var(--ink-soft); margin-top: 2px; }
  .rule { position: absolute; left: 322px; right: 0; top: 218px; height: 1px; background: var(--rule); }

  .contacts { position: absolute; left: 322px; top: 238px; list-style: none; }
  .contacts li {
    display: flex; align-items: center; gap: 12px; height: 26px;
    font-size: 15px; font-weight: 300; color: var(--ink-soft); letter-spacing: .3px;
  }
  .contacts svg { width: 16px; height: 16px; stroke: var(--ink-soft); fill: none; stroke-width: 1.4; }

  .band { position: absolute; left: 0; bottom: 0; width: 680px; height: 40px; }
</style>
</head>
<body>
<main class="stage">
  <section class="card card--front" aria-label="Card front">
    <div class="wordmark"><span class="wordmark__dot"></span>Brisco Interiors</div>
  </section>

  <section class="card card--back" aria-label="Card back">
    <div class="wordmark"><span class="wordmark__dot"></span>Brisco Interiors</div>
    <div class="person">
      <p class="person__name">Philippa Brisco</p>
      <p class="person__role">CEO &amp; Founder</p>
    </div>
    <div class="rule"></div>
    <ul class="contacts">
      <li>
        <svg viewBox="0 0 16 16"><path d="M4 2h2.5l1 3-1.6 1.2a8 8 0 0 0 3.9 3.9L11 8.5l3 1V12a2 2 0 0 1-2 2A10 10 0 0 1 2 4a2 2 0 0 1 2-2z"/></svg>
        +34 611.205.738
      </li>
      <li>
        <svg viewBox="0 0 16 16"><rect x="1.5" y="3.5" width="13" height="9"/><path d="M1.5 3.5 8 9l6.5-5.5"/></svg>
        hello@briscostudio.com
      </li>
      <li>
        <svg viewBox="0 0 16 16"><circle cx="8" cy="8" r="6.5"/><path d="M1.5 8h13M8 1.5c-3 3.5-3 9.5 0 13M8 1.5c3 3.5 3 9.5 0 13"/></svg>
        www.briscostudio.com
      </li>
    </ul>
    <svg class="band" viewBox="0 0 680 40" preserveAspectRatio="none" aria-hidden="true">
      <polygon points="300,0 680,0 680,40 318,40" fill="var(--band)"/>
    </svg>
  </section>
</main>
</body>
</html>
```